Book cover

I need a design for a book cover. Light back ground. On the front page a world enveloped by COVID-19 to which a stream of antibodies is going. Preferably waterpaint design.

Colors
0054AA
0677BA
7BADD7
CADEEF
E8F1F8
F0912C
F2A743
F7CA91
FBE8D2
FDF5EE

```html
<!DOCTYPE html>
<html lang="en">
<head>
<meta charset="utf-8">
<title>Antibody Based Treatment for SARS-CoV-2 — Book Cover</title>
<link rel="stylesheet" href="https://fonts.googleapis.com/css2?family=Cormorant+Garamond:wght@500;600&display=swap">
<style>
  :root {
    --page: #ffffff;
    --cover-light: #f3fbf5;
    --cover-mint: #def3e3;
    --title-blue: #1a6fb8;
    --ink: #333333;
    --rule: #3a3a3a;
    --virus-tone: rgba(76, 170, 40, 0.55);
    --virus-fade: rgba(76, 170, 40, 0);
    --globe-top: #3a6cb4;
    --globe-mid: #8fb0d8;
    --globe-low: #e6ebf0;
  }
  * { margin: 0; padding: 0; box-sizing: border-box; }
  html, body {
    width: 1200px; height: 1200px; overflow: hidden;
    background: var(--page);
  }
  .canvas { position: relative; width: 1200px; height: 1200px; }

  .book-spread {
    position: absolute; left: 56px; top: 237px;
    width: 1088px; height: 774px; overflow: hidden;
    background: radial-gradient(ellipse at 40% 45%, var(--cover-light) 0%, var(--cover-mint) 100%);
    font-family: "Cormorant Garamond", serif;
    font-variant-numeric: lining-nums;
  }

  .virus-decoration { position: absolute; inset: 0; }
  .virus-area {
    position: absolute; border-radius: 50%;
    background: radial-gradient(closest-side, var(--virus-tone), var(--virus-fade));
  }
  .virus-area--top-left     { left: -60px;  top: -90px;  width: 380px; height: 300px; }
  .virus-area--bottom-left  { left: -80px;  top: 460px;  width: 300px; height: 380px; }
  .virus-area--bottom-spine { left: 430px;  top: 690px;  width: 240px; height: 140px; }
  .virus-area--top-right    { left: 860px;  top: -60px;  width: 260px; height: 140px; }
  .virus-area--bottom-right { left: 990px;  top: 640px;  width: 160px; height: 180px; }

  .spine {
    position: absolute; left: 522px; top: 80px;
    width: 44px; height: 620px;
  }
  .spine-text {
    position: absolute; left: 44px; top: 0;
    transform-origin: 0 0; transform: rotate(90deg);
    width: 620px; height: 44px;
    display: flex; justify-content: space-between; align-items: center;
    white-space: nowrap; font-size: 18px; letter-spacing: 0.5px;
  }
  .spine-title { color: var(--title-blue); }
  .spine-sub { color: var(--ink); }
  .spine-author { color: var(--ink); letter-spacing: 1px; }

  .front-cover {
    position: absolute; left: 566px; top: 0; width: 522px; height: 774px;
  }
  .title {
    position: absolute; top: 70px; left: 0; width: 100%;
    text-align: center; font-weight: 500;
  }
  .title-main {
    display: block; color: var(--title-blue);
    font-size: 62px; line-height: 52px; letter-spacing: 2px;
  }
  .title-for {
    display: flex; align-items: center; justify-content: center; gap: 22px;
    color: var(--ink); font-size: 32px; line-height: 36px; margin-top: 6px;
  }
  .title-for::before, .title-for::after {
    content: ""; width: 114px; height: 3px; background: var(--rule);
  }
  .title-sub {
    display: block; color: var(--ink);
    font-size: 66px; line-height: 60px; letter-spacing: 2px;
  }

  .globe-art {
    position: absolute; left: 106px; top: 341px; width: 311px; height: 311px;
    border-radius: 50%;
    background: linear-gradient(160deg, var(--globe-top) 0%, var(--globe-mid) 55%, var(--globe-low) 100%);
  }
  .author {
    position: absolute; top: 708px; left: 0; width: 100%; text-align: center;
    font-weight: 600; font-size: 25px; letter-spacing: 2.5px; color: var(--ink);
  }
</style>
</head>
<body>
<div class="canvas">
  <div class="book-spread">
    <div class="virus-decoration" role="img" aria-label="Green coronavirus particle illustrations scattered around the cover edges">
      <div class="virus-area virus-area--top-left"></div>
      <div class="virus-area virus-area--bottom-left"></div>
      <div class="virus-area virus-area--bottom-spine"></div>
      <div class="virus-area virus-area--top-right"></div>
      <div class="virus-area virus-area--bottom-right"></div>
    </div>

    <div class="spine">
      <div class="spine-text">
        <span class="spine-title">ANTIBODY BASED TREATMENT <span class="spine-sub">for SARS-CoV-2</span></span>
        <span class="spine-author">MARLON DESSARAJ</span>
      </div>
    </div>

    <div class="front-cover">
      <h1 class="title">
        <span class="title-main">ANTIBODY<br>BASED<br>TREATMENT</span>
        <span class="title-for">for</span>
        <span class="title-sub">SARS-CoV-2</span>
      </h1>
      <div class="globe-art" role="img" aria-label="Illustration of planet Earth wearing a white respirator face mask with red straps"></div>
      <p class="author">MARLON DESSARAJ</p>
    </div>
  </div>
</div>
</body>
</html>
```